Quillspan

We need a 1 page flyer to showcase our public access phonebooth.
Meadowgate Outreach and Care Services
Connecting ones in need with loved ones
Flyer to indicate wired or wireless options.
The phone is VOIP based
LED lighting
Wireless option includes solar generation, and battery supply
Pictures need to be touched up to show warm summertime atmosphere
Ferncrest Color Pallette to be followed
www.ferncrestvoltix.com
email sales@ferncrestvoltix.com
Phone 780.555.0193

```html
<!DOCTYPE html>
<html lang="en">
<head>
<meta charset="utf-8">
<title>Quillspan Public Access Phonebooth Flyer</title>
<link rel="stylesheet" href="https://fonts.googleapis.com/css2?family=Roboto:ital,wght@0,300;0,400;0,500;0,700;1,300&family=Roboto+Condensed:ital,wght@1,700&display=swap">
<style>
  :root {
    --stage: #666666;
    --paper: #ffffff;
    --royal: #2c44a4;
    --royal-deep: #26399a;
    --navy-text: #2b3990;
    --sky: #4cc6ef;
    --leaf: #6cc04a;
    --steel-light: #c9d3de;
    --steel-dark: #5d6b80;
  }
  html, body {
    margin: 0;
    width: 1200px;
    height: 1200px;
    overflow: hidden;
    background: var(--stage);
  }
  .flyer {
    position: absolute;
    left: 233px;
    top: 125px;
    width: 733px;
    height: 949px;
    background: var(--paper);
    box-shadow: 0 14px 30px rgba(0,0,0,0.35);
    overflow: hidden;
  }
  .flyer svg { display: block; }
  .headline { font-family: "Roboto", sans-serif; font-weight: 700; fill: var(--paper); font-size: 90px; letter-spacing: -1.5px; }
  .tagline { font-family: "Roboto", sans-serif; font-weight: 300; font-style: italic; fill: var(--paper); font-size: 27px; }
  .brand-name { font-family: "Roboto", sans-serif; font-weight: 500; fill: var(--navy-text); font-size: 30px; }
  .option-main { font-family: "Roboto", sans-serif; font-weight: 500; fill: var(--navy-text); font-size: 50px; }
  .feature { font-family: "Roboto", sans-serif; font-weight: 400; fill: var(--navy-text); font-size: 24px; }
  .wireless-heading { font-family: "Roboto Condensed", sans-serif; font-weight: 700; font-style: italic; fill: var(--sky); font-size: 27px; }
  .wireless-item { font-family: "Roboto", sans-serif; font-weight: 400; fill: var(--navy-text); font-size: 15px; }
  .contact { font-family: "Roboto", sans-serif; font-weight: 500; fill: var(--paper); font-size: 14.5px; letter-spacing: 0.4px; }
  .icon-leaf { fill: none; stroke: var(--leaf); }
  .icon-navy { fill: var(--navy-text); }
</style>
</head>
<body>
<div class="flyer">
  <svg width="733" height="949" viewBox="0 0 733 949" xmlns="http://www.w3.org/2000/svg">
    <defs>
      <linearGradient id="booth-tone" x1="0" y1="0" x2="1" y2="1">
        <stop offset="0" stop-color="var(--steel-light)"/>
        <stop offset="0.45" stop-color="#2f56b8"/>
        <stop offset="1" stop-color="var(--steel-dark)"/>
      </linearGradient>
    </defs>

    <!-- blue header field -->
    <path class="header-field" d="M0 0 H733 V384 C560 410 420 470 0 626 Z" fill="var(--royal)"/>

    <!-- logo corner -->
    <ellipse class="logo-corner-rim" cx="0" cy="0" rx="288" ry="270" fill="var(--sky)"/>
    <ellipse class="logo-corner" cx="-6" cy="-4" rx="272" ry="266" fill="var(--paper)"/>
    <circle class="brand-dot" cx="28" cy="153" r="9" fill="var(--navy-text)"/>
    <text class="brand-name" x="44" y="164">Ferncrest</text>

    <!-- headline -->
    <text class="headline" x="712" y="123" text-anchor="end">PUBLIC</text>
    <text class="headline" x="712" y="212" text-anchor="end">ACCESS</text>
    <text class="headline" x="712" y="299" text-anchor="end">PHONEBOOTH</text>
    <text class="tagline" x="710" y="334" text-anchor="end">Connecting ones in need with loved ones</text>

    <!-- green footer wave -->
    <path class="footer-wave" d="M0 885 C180 860 380 800 560 818 C640 826 700 838 733 848 V949 H0 Z" fill="var(--leaf)"/>

    <!-- booth photo area -->
    <rect class="booth-photo" x="4" y="390" width="370" height="515" rx="4" fill="url(#booth-tone)" role="img" aria-label="Photo of the blue and stainless steel Quillspan public phone booth with Meadowgate Outreach and Care Services signage, in a warm summertime setting"/>

    <!-- wired / wireless -->
    <text class="option-main" x="646" y="508" text-anchor="end">WIRED</text>
    <g class="tick-badge" transform="translate(686 491)">
      <circle class="icon-leaf" r="21" stroke-width="5"/>
      <path d="M-11 -1 L-2 9 L20 -15" fill="none" stroke="var(--leaf)" stroke-width="7" stroke-linecap="round" stroke-linejoin="round"/>
    </g>
    <text class="option-main" x="646" y="566" text-anchor="end">WIRELESS</text>
    <g class="tick-badge" transform="translate(686 549)">
      <circle class="icon-leaf" r="21" stroke-width="5"/>
      <path d="M-11 -1 L-2 9 L20 -15" fill="none" stroke="var(--leaf)" stroke-width="7" stroke-linecap="round" stroke-linejoin="round"/>
    </g>

    <!-- features -->
    <text class="feature" x="678" y="630" text-anchor="end">VOIP BASED</text>
    <g class="phone-icon" transform="translate(689 612)">
      <path d="M2 2 C0 4 0 10 5 16 C10 22 15 24 18 22 L20 19 L15 15 L12 17 C10 16 7 13 6 10 L8 7 L5 2 Z" fill="var(--leaf)"/>
      <path d="M12 4 A7 7 0 0 1 18 10 M13 0 A11 11 0 0 1 22 9" fill="none" stroke="var(--leaf)" stroke-width="1.8"/>
    </g>
    <text class="feature" x="678" y="665" text-anchor="end">LED LIGHTING</text>
    <g class="led-icon" transform="translate(700 657)">
      <circle class="icon-leaf" r="11" stroke-width="2"/>
      <circle r="4" fill="var(--leaf)"/>
      <g fill="var(--leaf)">
        <circle cx="0" cy="-7.5" r="1.2"/><circle cx="0" cy="7.5" r="1.2"/>
        <circle cx="-7.5" cy="0" r="1.2"/><circle cx="7.5" cy="0" r="1.2"/>
        <circle cx="5.3" cy="5.3" r="1.2"/><circle cx="-5.3" cy="-5.3" r="1.2"/>
        <circle cx="5.3" cy="-5.3" r="1.2"/><circle cx="-5.3" cy="5.3" r="1.2"/>
      </g>
    </g>

    <!-- wireless option -->
    <text class="wireless-heading" x="711" y="732" text-anchor="end">WIRELESS OPTION INCLUDES</text>
    <text class="wireless-item" x="391" y="768">Solar Generation</text>
    <g class="solar-icon" transform="translate(522 754)" fill="var(--leaf)">
      <path d="M2 6 H18 L20 14 H0 Z"/>
      <path d="M6 6 L5 14 M10 6 V14 M14 6 L15 14 M1 10 H19" stroke="var(--paper)" stroke-width="1"/>
      <rect x="9" y="14" width="2" height="4"/>
      <circle cx="10" cy="2" r="2"/>
    </g>
    <text class="wireless-item" x="574" y="768">Battery Supply</text>
    <g class="battery-icon" transform="translate(690 758)">
      <rect width="19" height="11" fill="var(--leaf)"/>
      <rect x="19" y="3" width="2.5" height="5" fill="var(--leaf)"/>
      <path d="M10 2 L6 6 H9 L8 9 L13 5 H10 Z" fill="var(--paper)"/>
    </g>

    <!-- contacts -->
    <text class="contact" x="690" y="871" text-anchor="end">sales@ferncrestvoltix.com</text>
    <g class="mail-icon" transform="translate(698 862)">
      <rect width="13" height="9" class="icon-navy"/>
      <path d="M0 0 L6.5 5 L13 0" fill="none" stroke="var(--leaf)" stroke-width="1.2"/>
    </g>
    <text class="contact" x="690" y="893" text-anchor="end">ferncrestvoltix.com</text>
    <g class="globe-icon" transform="translate(705 888)" fill="none" stroke="var(--navy-text)" stroke-width="1.4">
      <circle r="6"/>
      <ellipse rx="2.6" ry="6"/>
      <path d="M-6 0 H6"/>
    </g>
    <text class="contact" x="690" y="915" text-anchor="end">780-555-0193</text>
    <g class="call-icon" transform="translate(699 904)">
      <path d="M1 1 C0 3 0 6 3 10 C6 13 9 14 11 13 L12 11 L9 9 L7 10 C6 9 4 7 4 5 L5 4 L3 1 Z" class="icon-navy"/>
    </g>
  </svg>
</div>
</body>
</html>
```